Website Landing Page for Brightfall Systems

Create a custom designed website landing page for our business. Looking for a professional upscale design that incorporates our logo and logo colors into the theme. I want a standard fixed frame website, not a constant scrolling format that seems to be the trend. To start with I'm looking for more of the graphic design part, maybe a concept or theme, I don't expect to see a finished project. Not interested in generic templates or layouts.

The name of our company is Brightfall Systems and I've attached our logo below. I'd like to have the web page have the same look and feel of our logo, as well as the colors. Our company, Brightfall Systems does system design, installation, and programming, of residential and commercial Audio/Video and Automation systems. We do home theaters, lighting and building automation, video conferencing systems, security camera installations, conference rooms, projectors, distributed audio systems, and similar Technology projects. This will be a professional services/informational website. We will not sell products on this website. This website will be used to advertise our company and communicate our services to prospective customers. Having a well designed, professional and clean website is one way we want to distinguish our company from the competition.

Here are some examples of what I consider a professional well designed website
http://www.qorlamstudio.com/Work/

Last year we had our tradlo store designed (with PixelMarket) and I'm really happy with the way it turned out. You can see it at www.HolvenGearDepot.com I consider this to be a great design and looking for the same level of quality with this new website. However, do not copy or use any part of this design in this new project. This tradlo store is completely separate from our other company Brightfall Systems. I only mention this tradlo store an an example of good work.

Reason: Still going through designs.

Reason: Still working on project and have not had time to review all designs and request revisions.

Reason: Sill going through designs and requesting revisions

Reason: still going through all the submissions we received.

Target Market(s)

People interested in Audio/Video, home theaters, home automation. We do sales, system design, and programming. We typically work on larger projects with both residential and commercial customers.

Industry/Entity Type

Business

Number of Pages Required

1 page

Requirements
Must have
• Great design elements. Please use a white background. I think white goes well with our logo colors.

```html
<!DOCTYPE html>
<html lang="en">
<head>
<meta charset="utf-8">
<title>Brightfall Systems — Landing Page</title>
<link href="https://fonts.googleapis.com/css2?family=Roboto:wght@300;400;500;700&display=swap" rel="stylesheet">
<style>
:root{
  --backdrop:#0d3447;
  --white:#ffffff;
  --blue:#1565c0;
  --blue-dark:#0d4a94;
  --green:#1aab45;
  --orange:#f39322;
  --text:#666a70;
  --muted:#9a9ea4;
  --line:#e4e6e9;
}
*{margin:0;padding:0;box-sizing:border-box}
html,body{width:1200px;height:1200px;overflow:hidden;background:var(--backdrop);font-family:'Roboto',Arial,sans-serif}
.page{position:absolute;left:332px;top:6px;width:483px;height:1194px;background:var(--white);overflow:hidden}
.abs{position:absolute}
/* top bar */
.topbar{left:0;top:0;width:483px;height:14px;background:var(--white);border-bottom:1px solid var(--line)}
.social-dot{width:5px;height:5px;border-radius:50%;background:var(--blue);top:4.5px}
.toplink{top:3.5px;font-size:5px;color:#445}
.register{left:380px;top:2px;width:29px;height:11px;border-radius:6px;background:var(--green);color:#fff;font-size:4.6px;text-align:center;line-height:11px}
.search{left:417px;top:3.5px}
/* hero */
.hero{left:0;top:14px;width:483px;height:264px;background:linear-gradient(100deg,#7f93b8 0%,#93a6c8 40%,#b8b3a6 75%,#9f9686 100%)}
.hero-shade{left:0;top:14px;width:483px;height:264px;background:linear-gradient(90deg,rgba(40,60,110,.45) 0%,rgba(40,60,110,.15) 60%,rgba(0,0,0,0) 100%)}
.logo-box{left:63px;top:21px;width:82px;height:34px;background:var(--white);display:flex;align-items:center;gap:4px;padding-left:6px}
.logo-mark{width:13px;height:13px;border-radius:50%;border:2px solid var(--blue);flex:none}
.logo-name{font-size:6.6px;font-weight:500;color:var(--blue);line-height:1.05;letter-spacing:.3px;text-transform:uppercase}
.nav{left:145px;top:26px;width:281px;height:16px;background:var(--blue)}
.nav-home{left:165px;top:26px;width:32px;height:16px;background:var(--green)}
.nav-item{top:31px;font-size:5px;color:#fff;letter-spacing:.2px}
.nav-login{left:388px;top:26px;width:38px;height:16px;background:var(--orange);color:#fff;font-size:5px;line-height:16px;padding-left:14px}
.kicker{left:64px;top:121px;font-size:6.6px;letter-spacing:1.8px;color:#fff}
.hero-title{left:63px;top:132px;font-size:21px;font-weight:300;color:#fff;letter-spacing:-.2px}
.hero-text{left:77px;top:162px;width:230px;font-size:6.8px;line-height:7.4px;color:#fff}
.btn{background:var(--green);color:#fff;text-align:center;font-weight:500}
.hero-btn{left:77px;top:193px;width:53px;height:15px;font-size:5.2px;line-height:15px}
.feat-white{left:63px;top:243px;width:117px;height:35px;background:var(--white);border-top:2px solid var(--orange)}
.feat-line{left:180px;top:243px;width:246px;height:2px;background:var(--blue)}
.feat-icon{width:26px;height:26px;border-radius:50%;background:var(--white);top:230px;display:flex;align-items:center;justify-content:center;box-shadow:0 1px 2px rgba(0,0,0,.15)}
.feat-label{top:259px;width:60px;text-align:center;font-size:6.4px;line-height:7px;color:#fff}
/* welcome */
.welcome{left:0;top:306px;width:483px;text-align:center;font-size:14.5px;color:var(--green)}
.welcome span{color:var(--blue)}
.welcome-text{left:74px;top:337px;width:340px;text-align:center;font-size:5.1px;line-height:9px;color:var(--text)}
/* services */
.tile{width:112px;height:100px;overflow:hidden}
.tile-label{left:5px;bottom:5px;color:#fff}
.tile-label b{display:block;font-size:5.2px;font-weight:500;text-transform:uppercase}
.tile-label i{display:block;font-style:normal;font-size:4.6px;margin-top:1px}
.more-btn{left:226px;top:627px;width:39px;height:16px;font-size:5.4px;line-height:16px}
/* guide band */
.band{left:0;top:664px;width:483px;height:105px;background:linear-gradient(180deg,#1a5fae,#1d6cc0)}
.band-title{left:0;top:681px;width:483px;text-align:center;font-size:14px;color:#fff}
.band-text{left:70px;top:702px;width:343px;text-align:center;font-size:5.1px;line-height:8px;color:#fff}
.download{left:217px;top:737px;width:54px;height:13px;border:1px solid #fff;border-radius:7px;color:#fff;font-size:4.8px;text-align:center;line-height:11px;font-weight:500}
/* news */
.news-title{left:0;top:788px;width:483px;text-align:center;font-size:14px;color:var(--blue)}
.news-rule{top:797px;width:22px;height:1px;background:var(--green)}
.card{width:110px;height:142px;top:818px;background:var(--white);box-shadow:0 1px 4px rgba(0,0,0,.15)}
.card-img{left:0;top:0;width:110px;height:60px}
.card-title{left:10px;top:67px;width:95px;font-size:8.8px;line-height:9.4px;color:var(--green)}
.card-date{left:10px;font-size:3.8px;color:var(--text)}
.card-text{left:10px;width:92px;font-size:3.8px;line-height:5.8px;color:var(--text)}
.card-more{left:10px;font-size:3.8px;color:var(--blue);font-weight:500}
.dot{top:978px;width:4px;height:4px;border-radius:50%;background:#c7c9cc}
.trouble{left:0;top:1001px;width:483px;text-align:center;font-size:14.5px;color:var(--blue)}
.help-btn{left:212px;top:1027px;width:60px;height:18px;font-size:5.4px;line-height:18px}
/* footer */
.f-head{top:1071px;font-size:7px;color:#555}
.f-link{font-size:4.6px;color:var(--muted)}
.f-logo{left:132px;top:1098px;display:flex;align-items:center;gap:4px}
.f-logo .logo-mark{width:17px;height:17px}
.f-input{left:314px;top:1096px;width:69px;height:13px;border:1px solid var(--line);font-size:4.4px;color:var(--muted);line-height:11px;padding-left:4px}
.f-sub{left:386px;top:1096px;width:31px;height:13px;background:#2aa1c9;color:#fff;font-size:4.4px;text-align:center;line-height:13px}
.f-rule{left:63px;top:1142px;width:363px;height:1px;background:var(--line)}
.f-social{top:1155px;width:9px;height:9px;border-radius:50%;background:#222}
.copyright{left:0;top:1177px;width:483px;text-align:center;font-size:4.6px;color:var(--text)}
</style>
</head>
<body>
<div class="page">

  <!-- top bar -->
  <div class="abs topbar"></div>
  <div class="abs social-dot" style="left:63px"></div>
  <div class="abs social-dot" style="left:71px"></div>
  <div class="abs social-dot" style="left:79px"></div>
  <div class="abs social-dot" style="left:87px"></div>
  <div class="abs toplink" style="left:316px">News</div>
  <div class="abs toplink" style="left:340px">Contact Us</div>
  <div class="abs register">Register</div>
  <svg class="abs search" width="7" height="7" viewBox="0 0 10 10"><circle cx="4" cy="4" r="3" fill="none" stroke="#222" stroke-width="1.4"/><line x1="6.2" y1="6.2" x2="9.2" y2="9.2" stroke="#222" stroke-width="1.4"/></svg>

  <!-- hero -->
  <div class="abs hero" role="img" aria-label="Technician in a hard hat installing a security camera on a building wall"></div>
  <div class="abs hero-shade"></div>

  <div class="abs nav"></div>
  <div class="abs nav-home"></div>
  <svg class="abs" style="left:176px;top:29px" width="10" height="9" viewBox="0 0 10 9"><path d="M5 0 L10 4.5 H8.5 V9 H6 V6 H4 V9 H1.5 V4.5 H0 Z" fill="#fff"/></svg>
  <div class="abs nav-item" style="left:206px">ABOUT US</div>
  <div class="abs nav-item" style="left:250px">SERVICES</div>
  <div class="abs nav-item" style="left:294px">CATEGORIES</div>
  <div class="abs nav-item" style="left:344px">TESTIMONIALS</div>
  <div class="abs nav-login">LOG IN</div>
  <svg class="abs" style="left:393px;top:31px" width="6" height="6" viewBox="0 0 6 6"><circle cx="3" cy="1.7" r="1.5" fill="#fff"/><path d="M0.4 6 C0.6 3.6 5.4 3.6 5.6 6Z" fill="#fff"/></svg>

  <div class="abs logo-box">
    <div class="logo-mark"></div>
    <div class="logo-name">Brightfall<br>Systems</div>
  </div>

  <div class="abs kicker">INTRODUCTION</div>
  <div class="abs hero-title">Security camera installations</div>
  <div class="abs hero-text">Lorem ipsum dolor sit amet, consectetur adipiscing elit. Aenean vehi cula eget quam sed hendrerit. In hac habitasse platea dictumst. Nunc vel sollicitudin enim</div>
  <div class="abs btn hero-btn">Get Started Now</div>

  <div class="abs feat-white"></div>
  <div class="abs feat-line"></div>
  <div class="abs feat-icon" style="left:100px">
    <svg width="13" height="13" viewBox="0 0 14 14"><path d="M3 1 L5.5 1 L6.5 4 L5 5 C5.8 7 7 8.2 9 9 L10 7.5 L13 8.5 V11 C13 12 12 13 11 13 C5.5 12.5 1.5 8.5 1 3 C1 2 2 1 3 1Z" fill="var(--blue)"/></svg>
  </div>
  <div class="abs feat-icon" style="left:237px">
    <svg width="11" height="13" viewBox="0 0 11 13"><rect x="2" y="1" width="7" height="11" rx="2" fill="none" stroke="#777" stroke-width="1.2"/><line x1="5.5" y1="3" x2="5.5" y2="6" stroke="#777" stroke-width="1.2"/></svg>
  </div>
  <div class="abs feat-icon" style="left:344px">
    <svg width="13" height="13" viewBox="0 0 14 14"><circle cx="7" cy="7" r="6" fill="none" stroke="#777" stroke-width="1.2"/><path d="M4 7.2 L6.2 9.3 L10 5" fill="none" stroke="#777" stroke-width="1.3"/></svg>
  </div>
  <div class="abs feat-label" style="left:83px;color:var(--blue);font-weight:500;font-size:5.8px">Free Tech<br>Support</div>
  <div class="abs feat-label" style="left:220px">Moderate<br>Price</div>
  <div class="abs feat-label" style="left:327px">Authorised<br>Dealer</div>

  <!-- welcome -->
  <div class="abs welcome">Welcome to <span>Brightfall Systems</span></div>
  <div class="abs welcome-text">Lorem ipsum dolor sit amet, consectetur adipiscing elit. Integer sed volutpat nulla, vel rhoncus ante. Lorem ipsum dolor sit amet, consectetur adipiscing elit. Integer sed volutpat nulla, vel rhoncus ante.Lorem ipsum dolor sit amet, consectetur adipiscing elit. Integer sed volutpat nulla, vel rhoncus ante.Lorem ipsum dolor sit amet, consectetur adipiscing elit. Integer sed volutpat nulla, vel rhoncus ante.Lorem ipsum dolor sit amet, consectetur adipiscing elit. Integer sed volutpat nulla, vel rhoncus ante.</div>

  <!-- services grid -->
  <div class="abs tile" style="left:63px;top:397px;background:linear-gradient(170deg,#1b3f9a 0%,#2a55b5 45%,#b8864a 75%,#3a3022 100%)" role="img" aria-label="Luxury house lit up at dusk with palm trees">
    <div class="abs tile-label"><b>Lighting and Building Automation</b><i>Lorem ipsum dolor sit amet</i></div></div>
  <div class="abs tile" style="left:188px;top:397px;background:linear-gradient(180deg,#8a6a56 0%,#6d5446 50%,#c9c6c3 80%,#9a9895 100%)" role="img" aria-label="Conference room with wall screen and meeting table">
    <div class="abs tile-label"><b>Video Conferencing Systems</b><i>Lorem ipsum dolor sit amet</i></div></div>
  <div class="abs tile" style="left:314px;top:397px;background:radial-gradient(circle at 35% 55%,#e6eef8 0%,#2b5fb0 30%,#0c1d4a 75%)" role="img" aria-label="Close-up of loudspeaker cones">
    <div class="abs tile-label"><b>Distributed Audio Systems</b><i>Lorem ipsum dolor sit amet</i></div></div>
  <div class="abs tile" style="left:63px;top:509px;background:linear-gradient(180deg,#d8d4cc 0%,#c8b59a 50%,#8f7a60 100%)" role="img" aria-label="Living room home theater with large screen">
    <div class="abs tile-label"><b style="font-weight:400">Home Theaters</b><i>Lorem ipsum dolor sit amet</i></div></div>
  <div class="abs tile" style="left:188px;top:509px;background:linear-gradient(135deg,#7f93b0 0%,#c8d2e0 50%,#eef0f4 100%)" role="img" aria-label="White security camera mounted on a wall">
    <div class="abs tile-label"><b style="font-weight:400">Security Camera Installations</b><i>Lorem ipsum dolor sit amet</i></div></div>
  <div class="abs tile" style="left:314px;top:509px;background:radial-gradient(circle at 85% 45%,#ffffff 0%,#8fc2ff 18%,#1e4f9a 50%,#081a45 100%)" role="img" aria-label="Projector lens emitting a bright beam">
    <div class="abs tile-label"><b style="font-weight:400">Projectors</b><i>Lorem ipsum dolor sit amet</i></div></div>

  <div class="abs btn more-btn">More info</div>

  <!-- guide band -->
  <div class="abs band" role="img" aria-label="Blue-tinted city skyline"></div>
  <div class="abs band-title">User Adoption Guide</div>
  <div class="abs band-text">Lorem ipsum dolor sit amet, consectetur adipiscing elit. Integer sed volutpat nulla, vel rhoncus ante. Lorem ipsum dolor sit amet, consectetur adipiscing elit. Integer sed volutpat nulla, vel rhoncus ante.Lorem ipsum dolor sit amet, consectetur adipiscing elit. Integer sed volutpat nulla, vel rhoncus ante.Lorem ipsum dolor sit amet, cons</div>
  <div class="abs download">DOWNLOAD ↓</div>

  <!-- news -->
  <div class="abs news-rule" style="left:180px"></div>
  <div class="abs news-title">Latest News</div>
  <div class="abs news-rule" style="left:296px"></div>

  <div class="abs card" style="left:72px">
    <div class="abs card-img" style="background:linear-gradient(135deg,#5a5d62 0%,#b07a45 50%,#d9a26a 100%)" role="img" aria-label="Cat drinking from a kitchen tap"></div>
    <div class="abs card-title">Laboris Eimod quis aliqua</div>
    <div class="abs card-date" style="top:88px">29th March</div>
    <div class="abs card-text" style="top:97px">Lorem ipsum dolor sit amet, consectetur adipi-scing elit. Integer sed volutpat nulla, vel rhon-</div>
    <div class="abs card-more" style="top:121px">READ MORE</div>
  </div>
  <div class="abs card" style="left:190px">
    <div class="abs card-img" style="background:linear-gradient(135deg,#e7c9bd 0%,#c98e7c 50%,#f2ddd6 100%)" role="img" aria-label="Child looking through a glass bowl"></div>
    <div class="abs card-title">Lorem ipsum amet</div>
    <div class="abs card-date" style="top:79px">29th March</div>
    <div class="abs card-text" style="top:88px">Lorem ipsum dolor sit amet, consectetur adipisc-ing elit. Integer sed volutpat nulla, vel rhoncus ante. Aenean eget malesuada massa. Sed plac-erat convallis nibh, ac aliquam nulla tristique quis. Donec nec nunc sed nulla</div>
    <div class="abs card-more" style="top:128px">READ MORE</div>
  </div>
  <div class="abs card" style="left:308px">
    <div class="abs card-img" style="background:linear-gradient(135deg,#9fb48a 0%,#6d8a52 45%,#c9a48c 100%)" role="img" aria-label="Family sharing a meal outdoors"></div>
    <div class="abs card-title">Laboris Eimod quis aliqua</div>
    <div class="abs card-date" style="top:88px">29th March, 2017</div>
    <div class="abs card-text" style="top:96px">Lorem ipsum dolor sit amet, consectetur adipisc-ing elit. Integer sed volutpat nulla, vel rhoncus</div>
    <div class="abs card-more" style="top:120px">READ MORE</div>
  </div>

  <div class="abs dot" style="left:235px"></div>
  <div class="abs dot" style="left:243px;background:var(--green)"></div>
  <div class="abs dot" style="left:251px"></div>

  <div class="abs trouble">Having trouble finding what you’re looking for?</div>
  <div class="abs btn help-btn">LET US HELP</div>

  <!-- footer -->
  <div class="abs f-head" style="left:71px">Quick Links</div>
  <div class="abs f-link" style="left:72px;top:1085px">Home</div>
  <div class="abs f-link" style="left:72px;top:1094px">Pricing &amp; Ordering</div>
  <div class="abs f-link" style="left:72px;top:1103px">Upcoming Courses</div>
  <div class="abs f-link" style="left:72px;top:1112px">Contact Us</div>
  <div class="abs f-link" style="left:71px;top:1122px;color:var(--blue)">See More Events</div>

  <div class="abs f-logo"><div class="logo-mark"></div><div class="logo-name" style="font-size:5.4px">Brightfall<br>Systems</div></div>

  <div class="abs f-head" style="left:217px">Contact Information</div>
  <svg class="abs" style="left:217px;top:1085px" width="5" height="5" viewBox="0 0 14 14"><path d="M3 1 L5.5 1 L6.5 4 L5 5 C5.8 7 7 8.2 9 9 L10 7.5 L13 8.5 V11 C13 12 12 13 11 13 C5.5 12.5 1.5 8.5 1 3 C1 2 2 1 3 1Z" fill="var(--orange)"/></svg>
  <div class="abs f-link" style="left:225px;top:1085px">Phone: +507 555 0142</div>
  <div class="abs f-link" style="left:225px;top:1094px">Alternate: +507 555 0187</div>
  <div class="abs f-link" style="left:225px;top:1103px">Email: info@brightfall.com</div>
  <svg class="abs" style="left:217px;top:1112px" width="5" height="6" viewBox="0 0 10 12"><path d="M5 0 C8 0 10 2 10 4.6 C10 7.5 5 12 5 12 C5 12 0 7.5 0 4.6 C0 2 2 0 5 0Z" fill="var(--orange)"/><circle cx="5" cy="4.5" r="1.8" fill="#fff"/></svg>
  <div class="abs f-link" style="left:225px;top:1112px">Harbor Tower #7</div>
  <div class="abs f-link" style="left:225px;top:1121px">Calle Marisol Vega</div>
  <div class="abs f-link" style="left:225px;top:1130px">Punta Lirio</div>

  <div class="abs f-head" style="left:314px">Sign Up for Newsletter</div>
  <div class="abs f-link" style="left:314px;top:1085px">Subscribe to our newsletter for regular updates</div>
  <div class="abs f-input">Enter Your Email address</div>
  <div class="abs f-sub">Subscribe</div>

  <div class="abs f-rule"></div>
  <div class="abs f-social" style="left:195px"></div>
  <div class="abs f-social" style="left:216px"></div>
  <div class="abs f-social" style="left:237px"></div>
  <div class="abs f-social" style="left:258px"></div>
  <div class="abs copyright">©Copyright 2003-2017, Brightfall Systems</div>
</div>
</body>
</html>
```